Webdesign for a Bikeshop in Veloria Kastwerk (male audience)

To obtain my master's degree, I am conducting a study in the field of web design as part of my master thesis. All submitted designs will therefore be used for study purposes. In order to achieve a homogeneous group, I would like to encourage not only male but also female web designers to submit a design. All submitted designs will be used anonymously for the study and therefore do not allow any conclusions to be drawn about your person. Since this is a contest, the winner will be chosen randomly from all serious submissions. I would be really happy if you would support me in my study. I think the results could be very informative and also useful for your further work (I won't go into more detail here as it could skew the results - but once the contest is over, feel free to contact me. Of course I will also provide you with my results as soon as my work is finished). Below you will find a fictitious usecase and a description of what the website should include:

The company Veloria Kastwerk is planning to relaunch its own website and would like to present itself primarily as a competent and leading consultant in the field of cargo bikes. The design should appeal to a broad audience and embody an urban lifestyle. In any case, the website should include a landing page, a product overview page and a product details page. The company also wants to appeal mainly to a MALE target group. You only design the website. So don't worry about hardware or software limitations, just create the best bike store design you can.

As it is fictitious, I can't offer any materials. A logo is not necessary, you can use a placeholder or whatever you have access to. If you need any inspring websites feel free to contact me.

Target Market(s)

male users

Number of Pages Required

1 page

Requirements
Must have
• landing page, product overview page, product details page
Should not have
• online shop

```html
<!DOCTYPE html>
<html lang="en">
<head>
<meta charset="utf-8">
<title>Veloria Kastwerk – Cargo Bikes</title>
<link rel="stylesheet" href="https://fonts.googleapis.com/css2?family=Audiowide&family=PT+Sans+Narrow:wght@400;700&display=swap">
<style>
:root{
  --yellow:#fff200;
  --black:#101010;
  --dark:#1e1e1e;
  --card:#333333;
  --footer:#232323;
  --footer-band:#1a1a1a;
  --white:#ffffff;
  --text-grey:#444444;
}
*{box-sizing:border-box;margin:0;padding:0}
html,body{width:1200px;height:3543px;overflow:hidden}
body{position:relative;background:var(--white);font-family:"PT Sans Narrow",sans-serif;color:var(--white)}
.abs{position:absolute}
.display{font-family:"Audiowide",sans-serif;font-weight:400}
.btn{position:absolute;background:var(--yellow);color:var(--black);font-weight:700;border-radius:5px;display:flex;align-items:center;justify-content:center;gap:8px}
.center{left:0;width:1200px;text-align:center}

/* nav */
.site-nav{top:0;left:0;width:1200px;height:99px;background:var(--black)}
.brand{left:145px;top:30px;font-size:32px;color:var(--white)}
.nav-link{top:36px;font-size:20px;color:var(--white)}
.nav-link.active{color:var(--yellow)}
.cart{left:896px;top:38px}
.cart-count{position:absolute;left:16px;top:-6px;width:11px;height:11px;border-radius:50%;background:var(--yellow);color:var(--black);font-size:8px;text-align:center;line-height:11px}

/* hero */
.hero{top:99px;left:0;width:1200px;height:553px;background:linear-gradient(135deg,#6f7468 0%,#545a52 40%,#7d7a50 65%,#3e4138 100%)}
.hero-shade{top:99px;left:0;width:1200px;height:553px;background:rgba(0,0,0,.25)}
.hero-kicker{top:248px;font-size:31px}
.hero-title{top:280px;font-size:66px;color:var(--yellow)}
.hero-text{top:377px;left:290px;width:620px;text-align:center;font-size:18px;line-height:28px}
.dots{top:616px;left:568px;display:flex;gap:8px;align-items:center}
.dots span{width:7px;height:7px;border-radius:50%;background:var(--white)}
.dots span.on{width:11px;height:11px;background:none;border:2px solid var(--white)}

/* featured */
.featured{top:652px;left:0;width:1200px;height:946px;background:var(--dark)}
.section-title{font-size:38px}
.product{width:214px}
.product-photo{height:206px;background:linear-gradient(180deg,#ffffff,#f3f3f3);border-radius:4px 4px 0 0;display:flex;align-items:center;justify-content:center}
.product-photo div{width:190px;height:90px;border-radius:8px;background:linear-gradient(90deg,#5a6068,#d7712a 40%,#c8642a 60%,#5a6068)}
.product-info{height:90px;background:var(--card);padding:8px 16px;border-radius:0 0 4px 4px}
.product-name{font-size:24px;line-height:30px}
.product-desc{font-size:11px;margin-top:4px}
.product-price{font-size:14px;font-weight:700;margin-top:6px}
.carousel-dot{width:28px;height:28px;border-radius:50%;background:var(--white)}
.lead{font-size:17px;line-height:29px;text-align:center}

/* about */
.about-title{left:145px;top:1658px;font-size:38px;color:var(--black)}
.about-text{left:146px;top:1726px;width:912px;font-size:17px;line-height:29px;color:var(--text-grey)}

/* video */
.video{top:1993px;left:0;width:1200px;height:544px;background:linear-gradient(120deg,#5d6a55 0%,#8a8160 35%,#a8c23a 55%,#8e7d62 75%,#6c6a5e 100%)}

/* gallery */
.gallery-title{top:2584px;font-size:38px;color:var(--black)}
.tile{position:absolute}
.g-green{background:linear-gradient(135deg,#4f6b2e,#9aa844)}
.g-street{background:linear-gradient(135deg,#7b7068,#4a4440)}
.g-snow{background:linear-gradient(135deg,#d6d8da,#8e9398)}
.g-brown{background:linear-gradient(135deg,#8b6547,#433a34)}

/* footer */
.footer{top:3220px;left:0;width:1200px;height:323px;background:var(--footer)}
.footer-brand{top:3242px;font-size:34px}
.footer-text{top:3298px;left:150px;width:900px;text-align:center;font-size:17px;line-height:27px}
.footer-link{top:3376px;font-size:20px}
.follow-band{top:3427px;left:370px;width:460px;height:40px;background:var(--footer-band)}
.follow{top:3436px;left:520px;font-size:16px;font-weight:700;display:flex;align-items:center;gap:10px}
.social{width:12px;height:12px;border-radius:50%;border:2px solid var(--white)}
.copyright{top:3490px;font-size:13px}
</style>
</head>
<body>

<header class="abs site-nav">
  <div class="abs brand display">Veloria Kastwerk</div>
  <nav>
    <span class="abs nav-link active" style="left:509px">Home</span>
    <span class="abs nav-link" style="left:598px">Shop</span>
    <span class="abs nav-link" style="left:680px">About Us</span>
    <span class="abs nav-link" style="left:797px">Contact</span>
    <span class="abs cart">
      <svg width="20" height="18" viewBox="0 0 20 18" fill="none" stroke="#fff" stroke-width="2"><path d="M1 2h3l2.5 10h10l2-7H5"/><circle cx="8" cy="15.5" r="1.3" fill="#fff"/><circle cx="15" cy="15.5" r="1.3" fill="#fff"/></svg>
      <span class="cart-count">2</span>
    </span>
  </nav>
  <div class="btn" style="left:954px;top:30px;width:86px;height:35px;font-size:20px">Login</div>
</header>

<section>
  <div class="abs hero" role="img" aria-label="Rider on a yellow cargo bike loaded with parcels, motion-blurred city street"></div>
  <div class="abs hero-shade"></div>
  <svg class="abs" style="left:72px;top:386px" width="22" height="34" viewBox="0 0 22 34"><path d="M18 3L5 17l13 14" fill="none" stroke="#fff" stroke-width="4"/></svg>
  <svg class="abs" style="left:1102px;top:386px" width="22" height="34" viewBox="0 0 22 34"><path d="M4 3l13 14L4 31" fill="none" stroke="#fff" stroke-width="4"/></svg>
  <div class="abs center hero-kicker display">Welcome to</div>
  <div class="abs center hero-title display">Veloria Kastwerk</div>
  <p class="abs hero-text">Lorem Ipsum is simply dummy text of the printing and typesetting industry. Lorem Ipsum has been the industry's standard dummy text ever since the 1500s.</p>
  <div class="btn" style="left:540px;top:451px;width:119px;height:33px;font-size:19px">Shop Now</div>
  <div class="abs dots"><span></span><span></span><span class="on"></span><span></span></div>
</section>

<section>
  <div class="abs featured"></div>
  <h2 class="abs center section-title display" style="top:722px">Featured Products</h2>

  <div class="abs carousel-dot" style="left:91px;top:925px"></div>
  <svg class="abs" style="left:100px;top:933px" width="10" height="12" viewBox="0 0 10 12"><path d="M7 1L2 6l5 5" fill="none" stroke="#111" stroke-width="2"/></svg>
  <div class="abs carousel-dot" style="left:1095px;top:925px"></div>
  <svg class="abs" style="left:1105px;top:933px" width="10" height="12" viewBox="0 0 10 12"><path d="M3 1l5 5-5 5" fill="none" stroke="#111" stroke-width="2"/></svg>

  <div class="abs product" style="left:145px;top:807px">
    <div class="product-photo" role="img" aria-label="Cargo bike with orange box"><div></div></div>
    <div class="product-info"><div class="product-name display">Cargo Bike</div><div class="product-desc">Lorem Ipsum is simply dummy text.</div><div class="product-price">$6,841.89</div></div>
  </div>
  <div class="abs product" style="left:377px;top:807px">
    <div class="product-photo" role="img" aria-label="Cargo bike with orange box"><div></div></div>
    <div class="product-info"><div class="product-name display">Cargo Bike</div><div class="product-desc">Lorem Ipsum is simply dummy text.</div><div class="product-price">$6,841.89</div></div>
  </div>
  <div class="abs product" style="left:609px;top:807px">
    <div class="product-photo" role="img" aria-label="Cargo bike with orange box"><div></div></div>
    <div class="product-info"><div class="product-name display">Cargo Bike</div><div class="product-desc">Lorem Ipsum is simply dummy text.</div><div class="product-price">$6,841.89</div></div>
  </div>
  <div class="abs product" style="left:842px;top:807px">
    <div class="product-photo" role="img" aria-label="Cargo bike with orange box"><div></div></div>
    <div class="product-info"><div class="product-name display">Cargo Bike</div><div class="product-desc">Lorem Ipsum is simply dummy text.</div><div class="product-price">$6,841.89</div></div>
  </div>

  <div class="btn" style="left:145px;top:1114px;width:214px;height:44px;font-size:15px"><svg width="22" height="18" viewBox="0 0 20 18" fill="none" stroke="#111" stroke-width="1.8"><path d="M1 2h3l2.5 10h10l2-7H5"/><circle cx="8" cy="15.5" r="1.3"/><circle cx="15" cy="15.5" r="1.3"/></svg>Buy Now</div>
  <div class="btn" style="left:377px;top:1114px;width:214px;height:44px;font-size:15px"><svg width="22" height="18" viewBox="0 0 20 18" fill="none" stroke="#111" stroke-width="1.8"><path d="M1 2h3l2.5 10h10l2-7H5"/><circle cx="8" cy="15.5" r="1.3"/><circle cx="15" cy="15.5" r="1.3"/></svg>Buy Now</div>
  <div class="btn" style="left:609px;top:1114px;width:214px;height:44px;font-size:15px"><svg width="22" height="18" viewBox="0 0 20 18" fill="none" stroke="#111" stroke-width="1.8"><path d="M1 2h3l2.5 10h10l2-7H5"/><circle cx="8" cy="15.5" r="1.3"/><circle cx="15" cy="15.5" r="1.3"/></svg>Buy Now</div>
  <div class="btn" style="left:842px;top:1114px;width:214px;height:44px;font-size:15px"><svg width="22" height="18" viewBox="0 0 20 18" fill="none" stroke="#111" stroke-width="1.8"><path d="M1 2h3l2.5 10h10l2-7H5"/><circle cx="8" cy="15.5" r="1.3"/><circle cx="15" cy="15.5" r="1.3"/></svg>Buy Now</div>

  <div class="btn" style="left:540px;top:1196px;width:119px;height:35px;font-size:19px">View All</div>

  <p class="abs lead" style="left:150px;top:1264px;width:900px">Lorem Ipsum is simply dummy text of the printing and typesetting industry. Lorem Ipsum has been the industry's standard dummy text ever since the 1500s, when an unknown printer took a galley of type and scrambled it to make a type specimen book. It has survived not only five centuries, but also the leap into electronic typesetting, remaining essentially unchanged. It was popularised in the 1960s with the release of Lettrafix sheets containing Lorem Ipsum passages, and more recently with desktop publishing software like Pagecraft Studio including versions of Lorem Ipsum.</p>
  <h2 class="abs center section-title display" style="top:1430px">That’s why you Choose Veloria Kastwerk Bike!</h2>
  <div class="btn" style="left:517px;top:1503px;width:167px;height:36px;font-size:19px">Make A Test Ride</div>
</section>

<section>
  <h2 class="abs about-title display">About Us</h2>
  <p class="abs about-text">Lorem Ipsum is simply dummy text of the printing and typesetting industry. Lorem Ipsum has been the industry's standard dummy text ever since the 1500s, when an unknown printer took a galley of type and scrambled it to make a type specimen book. It has survived not only five centuries, but also the leap into electronic typesetting, remaining essentially unchanged. It was popularised in the 1960s with the release of Lettrafix sheets containing Lorem Ipsum passages, and more recently with desktop publishing software like Pagecraft Studio including versions of Lorem Ipsum.</p>
  <div class="btn" style="left:145px;top:1898px;width:117px;height:35px;font-size:19px">Read More</div>
</section>

<section>
  <div class="abs video" role="img" aria-label="Video still: rider on a yellow cargo bike carrying stacked cardboard boxes"></div>
  <svg class="abs" style="left:566px;top:2242px" width="44" height="48" viewBox="0 0 44 48"><path d="M4 3l37 21L4 45z" fill="#fff"/></svg>
  <svg class="abs" style="left:1145px;top:2484px" width="20" height="20" viewBox="0 0 20 20" fill="none" stroke="#fff" stroke-width="2.5"><path d="M1 7V1h6M13 1h6v6M19 13v6h-6M7 19H1v-6"/></svg>
</section>

<section>
  <h2 class="abs center gallery-title display">Gallery</h2>
  <div class="tile g-green" style="left:145px;top:2663px;width:418px;height:132px" role="img" aria-label="Yellow cargo bike in a park"></div>
  <div class="tile g-street" style="left:577px;top:2663px;width:301px;height:272px" role="img" aria-label="Cargo bike with brown box on a street"></div>
  <div class="tile g-snow" style="left:892px;top:2663px;width:164px;height:130px" role="img" aria-label="Cargo bike carrying a fir tree in snow"></div>
  <div class="tile g-brown" style="left:145px;top:2806px;width:165px;height:129px" role="img" aria-label="Cargo bike at a crossing"></div>
  <div class="tile g-street" style="left:324px;top:2806px;width:240px;height:129px" role="img" aria-label="Cargo bike with parcels in town"></div>
  <div class="tile g-snow" style="left:891px;top:2806px;width:165px;height:129px" role="img" aria-label="Cargo bike seen from above on pavement"></div>
  <div class="tile g-street" style="left:147px;top:2946px;width:221px;height:218px" role="img" aria-label="Parent riding a black cargo bike with a child"></div>
  <div class="tile g-green" style="left:383px;top:2946px;width:289px;height:218px" role="img" aria-label="Family cycling on a park path"></div>
  <div class="tile g-green" style="left:689px;top:2946px;width:368px;height:218px" role="img" aria-label="Rider on a yellow cargo bike on a green path"></div>
</section>

<footer>
  <div class="abs footer"></div>
  <div class="abs center footer-brand display">Veloria Kastwerk</div>
  <p class="abs footer-text">Lorem Ipsum is simply dummy text of the printing and typesetting industry. Lorem Ipsum has been the industry's standard dummy text ever since the 1500s.</p>
  <span class="abs footer-link" style="left:346px">HOME</span>
  <span class="abs footer-link" style="left:481px">SHOP</span>
  <span class="abs footer-link" style="left:612px">ABOUT US</span>
  <span class="abs footer-link" style="left:782px">CONTACT</span>
  <div class="abs follow-band"></div>
  <div class="abs follow">Follow us : <span class="social"></span><span class="social"></span><span class="social"></span></div>
  <div class="abs center copyright">© copyrights 2022 Veloria Kastwerk | &nbsp;All Rights Reserved</div>
</footer>

</body>
</html>
```